Business Card Design

I am an child sleep consultant. I would like the picture to be the background of the card and for my logo to be in the upper right hand corner. Other than that, the design is yours!!

Industry/Entity Type

Business

Contact Information for Business Card

Marla Okonov
Tidewell Nestling
Certified Child Sleep Consultant
(406) 555-0193
tidewellnestling.example

```html
<!DOCTYPE html>
<html lang="en">
<head>
<meta charset="utf-8">
<title>Tidewell Nestling — Business Card</title>
<link rel="stylesheet" href="https://fonts.googleapis.com/css2?family=Source+Sans+3:wght@400;600;700&display=swap">
<style>
  :root {
    --page-bg: #ece9e4;
    --card-frame: #5798a6;
    --card-paper: #ffffff;
    --name-teal: #4e93a3;
    --title-khaki: #a5a27c;
    --contact-grey: #a8a491;
    --photo-light: #e6e3e6;
    --photo-mid: #b9b4ba;
    --photo-dark: #6f6a70;
  }
  * { box-sizing: border-box; margin: 0; padding: 0; }
  html, body {
    width: 1200px;
    height: 1014px;
    overflow: hidden;
    background: var(--page-bg);
    font-family: "Source Sans 3", "Source Sans Pro", sans-serif;
  }
  .stage {
    width: 1200px;
    height: 1014px;
    display: flex;
    align-items: center;
    justify-content: center;
  }
  .business-card {
    width: 1050px;
    height: 600px;
    background: var(--card-frame);
    padding: 24px;
    box-shadow: 0 6px 18px rgba(0,0,0,0.18);
  }
  .card-face {
    position: relative;
    width: 100%;
    height: 100%;
    background: var(--card-paper);
    display: flex;
  }
  .portrait-photo {
    width: 560px;
    height: 100%;
    background:
      radial-gradient(ellipse 45% 55% at 55% 50%, var(--photo-light) 0%, var(--photo-mid) 60%, transparent 100%),
      linear-gradient(160deg, var(--photo-light) 0%, var(--photo-mid) 45%, var(--photo-dark) 100%);
  }
  .card-info {
    position: relative;
    flex: 1;
  }
  .brand-mark {
    position: absolute;
    top: 34px;
    right: 40px;
    display: flex;
    align-items: center;
    gap: 12px;
    font-size: 30px;
    font-weight: 600;
    color: var(--name-teal);
  }
  .brand-mark__square {
    width: 22px;
    height: 22px;
    background: var(--title-khaki);
  }
  .contact-block {
    position: absolute;
    left: 40px;
    bottom: 46px;
    line-height: 1.18;
  }
  .contact-block__name {
    font-size: 36px;
    font-weight: 700;
    color: var(--name-teal);
  }
  .contact-block__title {
    font-size: 31px;
    font-weight: 700;
    color: var(--title-khaki);
  }
  .contact-block__details {
    margin-top: 14px;
    font-size: 24px;
    font-weight: 400;
    color: var(--contact-grey);
  }
</style>
</head>
<body>
  <main class="stage">
    <article class="business-card">
      <div class="card-face">
        <div class="portrait-photo" role="img" aria-label="Black and white photograph of a smiling baby looking upward"></div>
        <section class="card-info">
          <div class="brand-mark">
            <span class="brand-mark__square"></span>
            <span class="brand-mark__name">Tidewell Nestling</span>
          </div>
          <div class="contact-block">
            <p class="contact-block__name">Marla Okonov</p>
            <p class="contact-block__title">Tidewell Nestling Certified</p>
            <p class="contact-block__title">Child Sleep Consultant</p>
            <p class="contact-block__details">(406) 555-0193 • tidewellnestling.example</p>
          </div>
        </section>
      </div>
    </article>
  </main>
</body>
</html>
```